Online shopping mall needs a new webdesign

We recently had our logo redesigned and are looking for the perfect webdesign for our website. Important aspects are that we want to support small mobile devices (smartphones and small tablets) seperately, while also providing support for tablets upwards to desktop. Site will be built on bootstrap.
The full briefing is in the uploaded document.
Industry/Entity Type
Online Shopping
Logo Text
test
Number of Pages Required
5+ page
Look and feel

```html
<!DOCTYPE html>
<html lang="en">
<head>
<meta charset="utf-8">
<title>PayLater Shops – Blog/News</title>
<link href="https://fonts.googleapis.com/css2?family=Barlow:wght@400;500;600;700&display=swap" rel="stylesheet">
<style>
:root{
  --green:#97c21f;
  --green-dark:#7ba51a;
  --green-deep:#6e9416;
  --ink:#2b2b2b;
  --text:#6b6b6b;
  --muted:#9a9a9a;
  --line:#e4e4e4;
  --page:#f6f6f6;
  --footer:#333333;
  --footer-bottom:#2a2a2a;
  --teal:#95ded6;
  --teal-soft:#a9e5de;
  --white:#ffffff;
}
*{box-sizing:border-box;margin:0;padding:0}
html,body{width:1200px;height:2799px;overflow:hidden}
body{font-family:"Barlow",Arial,sans-serif;color:var(--text);background:var(--white);position:relative;font-size:12px}
a{color:inherit;text-decoration:none}
.wrap{position:absolute;left:155px;width:890px}

/* cookie bar */
.cookie-bar{position:absolute;top:0;left:0;width:1200px;height:63px;background:var(--ink);display:flex;align-items:center;justify-content:center;gap:18px;color:var(--white);font-size:13px}
.cookie-bar .btn{background:var(--green);color:var(--white);border-radius:14px;padding:6px 20px;font-weight:600;font-size:12px}

/* top bar */
.top-bar{top:63px;height:40px;display:flex;align-items:center;justify-content:space-between;border-bottom:1px solid var(--line);font-size:12px;color:var(--muted)}
.top-bar .contact{display:flex;align-items:center;gap:8px}
.top-links{display:flex;align-items:center;gap:10px}
.top-links .active{color:var(--green)}
.like-box{display:flex;gap:4px;margin-left:20px}
.like-box span{display:block;height:18px;border-radius:2px}

/* header */
.header{top:103px;height:104px;display:flex;align-items:center;justify-content:space-between}
.logo{display:flex;flex-direction:column}
.logo-row{display:flex;align-items:center;gap:8px}
.logo-mark{width:28px;height:28px;border-radius:50%;background:var(--green)}
.logo-name{font-size:17px;font-weight:600;color:var(--ink)}
.logo-tag{font-size:11px;color:var(--green);margin-left:36px}
.search{width:380px;height:34px;border:1px solid var(--line);border-radius:17px;display:flex;align-items:center;justify-content:space-between;padding:0 16px;color:#bbb;font-size:11px}
.btn-outline{border:2px solid var(--green);border-radius:18px;padding:9px 20px;color:var(--green-dark);font-size:11px;font-weight:600;letter-spacing:.5px}

/* nav */
.main-nav{position:absolute;top:209px;left:0;width:1200px;height:40px;background:var(--green)}
.main-nav .wrap{height:40px;display:flex;align-items:center;color:var(--white);font-size:13px;font-weight:600}
.main-nav .item{height:40px;display:flex;align-items:center;justify-content:center;width:213px}
.main-nav .item.active{background:var(--green-dark)}
.main-nav .item.sales{position:absolute;right:4px;width:146px;background:var(--green-deep);height:48px;top:-8px;padding-top:6px;clip-path:polygon(0 16%,50% 0,100% 16%,100% 100%,0 100%)}

/* hero */
.page-head{position:absolute;top:420px;left:0;width:1200px;height:274px;background:var(--page);box-shadow:0 6px 8px rgba(0,0,0,.06)}
.banners{top:272px;height:200px;display:flex;justify-content:space-between}
.banner-photo{width:584px;height:200px;background:linear-gradient(120deg,#6f7f8f,#c9a98e 45%,#2f6fb5 70%,#e0c632)}
.banner-ad{width:280px;height:200px;background:var(--teal);display:flex;flex-direction:column;align-items:center;padding-top:22px}
.banner-ad .product{width:170px;height:96px;background:var(--teal-soft);margin-bottom:14px}
.banner-ad h3{font-size:17px;font-weight:700;color:var(--ink);line-height:1.2}
.banner-ad p{font-size:11px;color:#c42525;font-weight:600}
.breadcrumb{top:500px;height:30px;border-bottom:1px solid var(--line);font-size:12px;color:var(--ink);display:flex;align-items:center;gap:8px}
.intro{top:553px}
.intro h1{font-size:28px;font-weight:500;color:var(--green);margin-bottom:10px}
.intro p{font-size:12px;line-height:1.5;color:var(--text)}

/* results bar */
.results{display:flex;align-items:center;height:24px;font-size:10px;letter-spacing:.5px}
.results .count{width:193px;height:24px;border:1px solid #d6d6d6;display:flex;align-items:center;padding-left:10px;color:var(--muted)}
.results .select{width:60px;height:24px;background:#c9c9c9;color:var(--white);display:flex;align-items:center;padding-left:10px}

/* cards */
.grid{top:810px;display:grid;grid-template-columns:431px 431px;gap:24px 28px}
.card{background:var(--white);height:407px;box-shadow:0 1px 3px rgba(0,0,0,.08)}
.card.hover{box-shadow:0 4px 12px rgba(0,0,0,.16)}
.card-media{height:200px;position:relative}
.card-label{position:absolute;left:24px;bottom:12px;color:var(--white);font-size:10px;font-weight:600;display:flex;align-items:center;gap:5px}
.card-body{padding:20px 24px}
.card-title{font-size:19px;font-weight:500;color:var(--ink);line-height:1.3;margin-bottom:10px}
.card.hover .card-title{text-decoration:underline}
.card-meta{font-size:10px;color:var(--muted);display:flex;gap:8px;margin-bottom:18px}
.card-text{font-size:11.5px;line-height:1.45;color:var(--text)}
.card-arrow{margin-top:18px;color:var(--muted)}
.card.hover .card-arrow{color:var(--green)}

.pager{top:2123px;display:flex;justify-content:space-between;align-items:center}
.pages{display:flex;gap:8px}
.pages span{width:26px;height:26px;border-radius:50%;background:#ddd;color:var(--white);display:flex;align-items:center;justify-content:center;font-size:11px}
.pages .on{background:var(--green)}

/* cta */
.cta{position:absolute;top:2249px;left:0;width:1200px;height:134px;background:var(--green)}
.cta .wrap{top:32px;display:flex;justify-content:space-between;align-items:center;color:var(--white)}
.cta h2{font-size:24px;font-weight:600;margin-bottom:4px}
.cta p{font-size:13px;line-height:1.35;width:580px}
.cta .btn-outline{border-color:var(--white);color:var(--white)}

/* footer */
.footer{position:absolute;top:2383px;left:0;width:1200px;height:353px;background:var(--footer)}
.footer .wrap{top:58px;display:grid;grid-template-columns:228px 229px 228px 205px;color:#ccc}
.footer h4{font-size:14px;font-weight:500;color:var(--white);margin-bottom:14px}
.footer li{list-style:none;font-size:11px;line-height:19px}
.footer li::before{content:"›";margin-right:7px;color:var(--white)}
.footer address{font-style:normal;font-size:11px;line-height:16px}
.footer .phone{font-size:19px;color:#ddd;margin:18px 0 6px}
.footer .mail{font-size:12px;color:var(--green);text-decoration:underline}
.footer .social-title{font-size:11px;margin-top:22px}
.socials{display:flex;gap:9px;margin-top:6px}
.socials span{width:10px;height:10px;border-radius:50%;background:#ccc}
.bottom-bar{position:absolute;top:2736px;left:0;width:1200px;height:63px;background:var(--footer-bottom)}
.bottom-bar .wrap{height:63px;display:flex;align-items:center;justify-content:space-between;font-size:11px;color:#aaa}
.seal{width:66px;height:28px;border-radius:14px;background:var(--white)}
.cards{display:flex;gap:5px}
.cards span{width:40px;height:26px;background:var(--white);border-radius:2px}
.to-top{position:absolute;right:70px;top:18px;width:28px;height:28px;background:var(--green);transform:rotate(45deg)}
</style>
</head>
<body>

<div class="cookie-bar">
  <span>Due to law we need to ask you if you want our cookies.</span>
  <a class="btn" href="#">Yes, of Course</a>
  <a class="btn" href="#">No</a>
</div>

<div class="wrap top-bar">
  <div class="contact">
    <svg width="14" height="14" viewBox="0 0 24 24"><path fill="#97c21f" d="M6.6 10.8a15 15 0 006.6 6.6l2.2-2.2a1 1 0 011-.25 11.4 11.4 0 003.6.57 1 1 0 011 1V20a1 1 0 01-1 1A17 17 0 013 4a1 1 0 011-1h3.5a1 1 0 011 1c0 1.25.2 2.45.57 3.57a1 1 0 01-.25 1z"/></svg>
    <span>+31 6 1234 5678</span><span>/</span><span>E: info@greenwaymedia.nl</span>
  </div>
  <div class="top-links">
    <a href="#">Home</a><span>/</span><a href="#">About Us</a><span>/</span><a class="active" href="#">Blog</a><span>/</span><a href="#">Contact Us</a>
    <div class="like-box"><span style="width:44px;background:#3b5998"></span><span style="width:24px;border:1px solid #ccc"></span></div>
  </div>
</div>

<header class="wrap header">
  <div class="logo">
    <div class="logo-row"><span class="logo-mark"></span><span class="logo-name">PayLater-Shops.nl</span></div>
    <span class="logo-tag">Koop nu, betaal later</span>
  </div>
  <div class="search"><span>Search Here ...</span>
    <svg width="12" height="12" viewBox="0 0 24 24"><circle cx="10" cy="10" r="7" fill="none" stroke="#97c21f" stroke-width="3"/><path d="M15 15l6 6" stroke="#97c21f" stroke-width="3"/></svg>
  </div>
  <a class="btn-outline" href="#">REGISTER WEBSHOP</a>
</header>

<nav class="main-nav">
  <div class="wrap">
    <a class="item active" href="#">PayLater Shops</a>
    <a class="item" href="#">Payment Methods</a>
    <a class="item" href="#">Quality Marks</a>
    <a class="item sales" href="#">SALES/DISCOUNT</a>
  </div>
</nav>

<div class="page-head"></div>

<div class="wrap banners">
  <div class="banner-photo" role="img" aria-label="Photo of a smiling couple with colourful shopping bags and a tablet"></div>
  <div class="banner-ad">
    <div class="product" role="img" aria-label="Illustration of a portable speaker with a 20% off sticker"></div>
    <h3>PORTABLE SPEAKER</h3>
    <p>GENUINE PRODUCTS</p>
  </div>
</div>

<div class="wrap breadcrumb"><span>PayLater Shops</span><span>»</span><span>Blog</span></div>

<section class="wrap intro">
  <h1>Blog/News</h1>
  <p>Lorem Ipsum has been the industry's standard dummy text ever since the 1500s, when an unknown printer took a galley of type and scrambled it to make a type specimen book. It has survived not only five centuries, but also the leap into electronic typesetting, remaining essentially unchanged.</p>
</section>

<div class="wrap results" style="top:759px">
  <span class="count">SHOWING 1 – 9 OF 57 RESULTS</span><span class="select">100 ▾</span>
</div>

<main class="wrap grid">
  <article class="card">
    <div class="card-media" role="img" aria-label="Photo of a woman with glasses asleep on a book" style="background:linear-gradient(135deg,#c79a74,#8a5a3e 60%,#e6c9a8)"><span class="card-label">▮ BLOG</span></div>
    <div class="card-body"><h2 class="card-title">Lorem Ipsum has been the industry's standard dummy text ever since</h2><div class="card-meta"><span>▦ 26 SEP, 2016</span><span>/</span><span>● LOREM IPSUM</span></div><p class="card-text">Lorem Ipsum has been the industry's standard dummy text ever since the 1500s, when an unknown printer took a galley of type and scrambled it to make a type specimen book ...</p><div class="card-arrow">→</div></div>
  </article>
  <article class="card hover">
    <div class="card-media" role="img" aria-label="Photo of a woman with a pink umbrella in a city square" style="background:linear-gradient(135deg,#8a8580,#c9b8aa 50%,#d9466a)"><span class="card-label">▮ NEWS</span></div>
    <div class="card-body"><h2 class="card-title">Lorem Ipsum has been the industry's standard dummy text ever since</h2><div class="card-meta"><span>▦ 26 SEP, 2016</span><span>/</span><span>● LOREM IPSUM</span></div><p class="card-text">Lorem Ipsum has been the industry's standard dummy text ever since the 1500s, when an unknown printer took a galley of type and scrambled it to make a type specimen book ...</p><div class="card-arrow">→</div></div>
  </article>
  <article class="card">
    <div class="card-media" role="img" aria-label="Photo of a skier walking through a snowy forest" style="background:linear-gradient(180deg,#2f3a30,#7a8a80 45%,#e8ecef)"><span class="card-label">▮ BLOG</span></div>
    <div class="card-body"><h2 class="card-title">Lorem Ipsum has been the industry's standard dummy text ever since</h2><div class="card-meta"><span>▦ 26 SEP, 2016</span><span>/</span><span>● LOREM IPSUM</span></div><p class="card-text">Lorem Ipsum has been the industry's standard dummy text ever since the 1500s, when an unknown printer took a galley of type and scrambled it to make a type specimen book ...</p><div class="card-arrow">→</div></div>
  </article>
  <article class="card">
    <div class="card-media" role="img" aria-label="Photo of a wakeboarder splashing across the water" style="background:linear-gradient(135deg,#3a3c3a,#6f7571 50%,#dfe3e4)"><span class="card-label">▮ BLOG</span></div>
    <div class="card-body"><h2 class="card-title">Lorem Ipsum has been the industry's standard dummy text ever since</h2><div class="card-meta"><span>▦ 26 SEP, 2016</span><span>/</span><span>● LOREM IPSUM</span></div><p class="card-text">Lorem Ipsum has been the industry's standard dummy text ever since the 1500s, when an unknown printer took a galley of type and scrambled it to make a type specimen book ...</p><div class="card-arrow">→</div></div>
  </article>
  <article class="card">
    <div class="card-media" role="img" aria-label="Photo of an artist painting a large colourful street mural" style="background:linear-gradient(135deg,#2b6f8f,#b9773f 50%,#3c5f7a)"><span class="card-label">▮ NEWS</span></div>
    <div class="card-body"><h2 class="card-title">Lorem Ipsum has been the industry's standard dummy text ever since</h2><div class="card-meta"><span>▦ 26 SEP, 2016</span><span>/</span><span>● LOREM IPSUM</span></div><p class="card-text">Lorem Ipsum has been the industry's standard dummy text ever since the 1500s, when an unknown printer took a galley of type and scrambled it to make a type specimen book ...</p><div class="card-arrow">→</div></div>
  </article>
  <article class="card">
    <div class="card-media" role="img" aria-label="Photo of a girl running through a meadow with balloons" style="background:linear-gradient(135deg,#6b5a3a,#d6b451 45%,#f1a43a)"><span class="card-label">▮ BLOG</span></div>
    <div class="card-body"><h2 class="card-title">Lorem Ipsum has been the industry's standard dummy text ever since</h2><div class="card-meta"><span>▦ 26 SEP, 2016</span><span>/</span><span>● LOREM IPSUM</span></div><p class="card-text">Lorem Ipsum has been the industry's standard dummy text ever since the 1500s, when an unknown printer took a galley of type and scrambled it to make a type specimen book ...</p><div class="card-arrow">→</div></div>
  </article>
</main>

<div class="wrap pager">
  <div class="results"><span class="count">SHOWING 1 – 9 OF 57 RESULTS</span><span class="select">100 ▾</span></div>
  <div class="pages"><span>‹</span><span class="on">1</span><span>2</span><span>3</span><span class="on">›</span></div>
</div>

<section class="cta">
  <div class="wrap">
    <div>
      <h2>PayLater Shops 100% safe online shopping!</h2>
      <p>Online shopping at webshops PayLater is absolutely 100% safe. No fuss or malicious web shops that do not deliver your order!</p>
    </div>
    <a class="btn-outline" href="#">REGISTER NOW!</a>
  </div>
</section>

<footer class="footer">
  <div class="wrap">
    <div><h4>Quick Link</h4><ul><li>Home</li><li>About Us</li><li>Deparment overview</li><li>Quality marks</li><li>Sales/Discount</li><li>Blog</li><li>Informational</li><li>Contact Us</li><li>Sitemap</li></ul></div>
    <div><h4>PayLater Shops</h4><ul><li>Electronics &amp; Home Appliances</li><li>Clothing &amp; Fashion</li><li>Beauty &amp; Health</li><li>Etc.</li></ul></div>
    <div><h4>Payment Methods</h4><ul><li>PayLater</li><li>Klarvo</li><li>Bucketpay</li><li>Vista Card</li><li>Mastermint</li><li>Etc.</li></ul></div>
    <div><h4>Contact Info</h4>
      <address>Greenway Online Media<br>Lindelaan 14 1234 AB<br>ZANDHOVEN</address>
      <div class="phone">Call: +31 6 1234 5678</div>
      <a class="mail" href="#">info@greenwaymedia.nl</a>
      <div class="social-title">Get Social:</div>
      <div class="socials"><span></span><span></span><span></span><span></span></div>
    </div>
  </div>
</footer>

<div class="bottom-bar">
  <div class="wrap">
    <span>Copyright © 2016, PayLater Shops. All Rights Reserved.</span>
    <span class="seal"></span>
    <div class="cards"><span></span><span></span><span></span><span></span><span></span></div>
  </div>
  <span class="to-top"></span>
</div>

</body>
</html>
```